Breast Cancer Car Donation Website Design

Please create a new one page website design.

Current site: http://www.givemyautohope.com/

The NEW website address will be RidesforPinkRibbonAid.org

Use these sites for an idea of what I am looking for. I like these sites best: drivesforheroesfund.org and autosforservicemen.org

```html
<!DOCTYPE html>
<html lang="en">
<head>
<meta charset="utf-8">
<title>Rides for Pink Ribbon Aid – Donate a Car or Boat</title>
<link href="https://fonts.googleapis.com/css2?family=Roboto+Condensed:wght@400;700&family=Roboto:wght@400;500&display=swap" rel="stylesheet">
<style>
:root{
  --pink:#e6136f;
  --ink:#222226;
  --grey:#6d6d6d;
  --blue:#3aa0d8;
  --nav:#4a4a4a;
  --field:#ffffff;
  --footer:#2b2b2b;
  --band:#efefef;
  --line:#dcdcdc;
}
*{box-sizing:border-box;margin:0;padding:0}
html,body{width:714px;height:1200px;overflow:hidden;background:#fff}
body{position:relative;font-family:"Roboto Condensed",Arial,sans-serif;color:var(--ink)}
.abs{position:absolute}

/* brand name: plain text with one plain dot */
.brand{display:flex;align-items:center;gap:7px;font-family:"Roboto Condensed",Arial,sans-serif;font-weight:400;color:var(--ink);white-space:nowrap}
.brand-dot{width:11px;height:11px;border-radius:50%;background:var(--pink);flex:none}

/* header */
.site-header .brand{left:96px;top:12px;font-size:20px}
.call{left:440px;top:14px;width:178px;height:22px;border:1px solid #ddd;border-radius:11px;font-size:8px;font-weight:700;color:var(--pink);padding:6px 0 0 13px}
.call-icon{right:-1px;top:-1px;width:22px;height:22px;border-radius:50%;background:#161630;display:flex;align-items:center;justify-content:center}

/* nav */
.main-nav{left:0;top:49px;width:714px;height:21px;background:var(--nav)}
.main-nav a{position:absolute;top:0;height:21px;line-height:21px;font-size:7px;font-weight:700;color:#fff;text-decoration:none}
.main-nav .active{left:96px;width:110px;background:var(--pink);text-align:center}
.main-nav .donate{left:568px;width:50px;background:var(--pink);text-align:center}

/* hero */
.hero{left:0;top:70px;width:714px;height:276px;background:linear-gradient(100deg,#3c3e44 0%,#8a8d92 30%,#cfd3d8 55%,#a9aeb4 80%,#d9dcdf 100%)}
.donor-form{left:0;top:198px;width:714px;height:148px;background:rgba(40,40,44,.72)}
.donor-form h2{position:absolute;left:96px;top:12px;font-size:11px;font-weight:700;color:#fff}
.donor-form p{position:absolute;left:96px;font-size:8px;color:#fff}
.field{position:absolute;height:19px;background:var(--field);border-radius:2px;font-family:Roboto,Arial,sans-serif;font-size:5.5px;color:#888;padding:6px 0 0 7px}
.field.sel::after{content:"";position:absolute;right:5px;top:8px;border:2.5px solid transparent;border-top:3px solid #555}
.submit{position:absolute;height:19px;background:var(--pink);color:#fff;font-size:7.5px;font-weight:700;text-align:center;line-height:19px;border-radius:2px}

/* how */
.how-title{left:0;width:714px;top:382px;text-align:center;font-size:18px;font-weight:700}
.pink{color:var(--pink)}
.body-text{font-family:Roboto,Arial,sans-serif;font-size:5.6px;line-height:10px;color:var(--grey);text-align:center}
.sub-title{left:0;width:714px;top:454px;text-align:center;font-size:8.5px;font-weight:500}
.sub-title span{color:var(--blue);font-weight:700}

/* donate strip */
.donate-strip{left:96px;top:539px;width:522px;height:37px;border-top:1px solid var(--line);border-bottom:1px solid var(--line)}
.donate-strip .label{position:absolute;left:15px;top:9px;font-size:16px;font-weight:700}
.perk{position:absolute;top:9px;display:flex;gap:6px;align-items:center;font-size:7.5px;font-weight:700;line-height:9px}

/* why */
.why-title{left:112px;top:608px;font-size:21px;font-weight:700;line-height:32px}
.why-title .soft{color:#cfcfcf}
.why-list{left:266px;top:614px;list-style:none}
.why-list li{display:flex;align-items:center;gap:6px;height:15.6px;font-family:Roboto,Arial,sans-serif;font-size:5.6px;color:var(--grey)}
.why-list b{color:var(--ink);font-family:"Roboto Condensed",Arial,sans-serif;font-size:6.5px}

/* faq */
.faq{left:0;top:740px;width:714px;height:224px;background:linear-gradient(160deg,#5a2438 0%,#7a3a52 45%,#5e2a3c 100%)}
.faq h2{position:absolute;left:0;width:714px;top:35px;text-align:center;color:#fff;font-size:13px;font-weight:700}
.faq .rule{position:absolute;left:347px;top:56px;width:20px;height:2px;background:var(--pink)}
.faq-card{position:absolute;top:74px;width:249px;height:108px;background:#fff}
.faq-card div{height:27px;border-bottom:1px solid #ececec;display:flex;align-items:center;font-size:6.5px;font-weight:700;padding-left:8px;gap:13px}
.faq-card div:last-child{border-bottom:0}
.plus{width:9px;height:9px;background:#eee;color:#999;font-size:8px;line-height:9px;text-align:center;font-weight:400}

/* logo band */
.logo-band{left:0;top:964px;width:714px;height:74px;background:var(--band)}
.logo-band .brand{position:absolute;left:0;width:714px;justify-content:center;top:25px;font-size:17px}

/* footer */
.site-footer{left:0;top:1038px;width:714px;height:140px;background:var(--footer);color:#fff}
.site-footer h3{position:absolute;top:27px;font-size:8px;font-weight:400;font-family:Roboto,Arial,sans-serif}
.foot-nav{position:absolute;left:96px;top:45px;list-style:none;font-family:Roboto,Arial,sans-serif;font-size:5.5px;color:#aaa;line-height:12px}
.about{position:absolute;left:194px;top:45px;width:250px;font-family:Roboto,Arial,sans-serif;font-size:5.5px;color:#aaa;line-height:9px}
.contact-box{position:absolute;left:457px;top:28px;width:161px;height:77px;border:1.5px solid #ddd;font-family:Roboto,Arial,sans-serif;font-size:5.5px;color:#aaa;padding:14px 0 0 15px}
.contact-box p{margin-bottom:8px}
.contact-box .val{color:#fff;font-size:7px;margin-left:6px}
.social{display:flex;gap:4px;margin-top:2px}
.social span{width:14px;height:14px;border-radius:1px}
.copyright{left:0;top:1178px;width:714px;height:22px;background:var(--pink);color:#fff;font-family:Roboto,Arial,sans-serif;font-size:5.5px;text-align:center;line-height:22px}
</style>
</head>
<body>

<header class="site-header">
  <div class="abs brand"><span class="brand-dot"></span>Rides for Pink Ribbon Aid</div>
  <div class="abs call">CALL TODAY TO DONATE : 1-555-240-7713
    <span class="abs call-icon"><svg width="10" height="10" viewBox="0 0 24 24"><path fill="#fff" d="M6.6 10.8a15 15 0 0 0 6.6 6.6l2.2-2.2c.3-.3.7-.4 1-.2 1.1.4 2.3.6 3.6.6.6 0 1 .4 1 1V20c0 .6-.4 1-1 1A17 17 0 0 1 3 4c0-.6.4-1 1-1h3.5c.6 0 1 .4 1 1 0 1.3.2 2.5.6 3.6.1.3 0 .7-.2 1z"/></svg></span>
  </div>
</header>

<nav class="abs main-nav">
  <a class="active" href="#">DONATE A CAR OR BOAT NOW</a>
  <a style="left:218px" href="#">ABOUT US</a>
  <a style="left:273px" href="#">CONTACT US</a>
  <a style="left:336px" href="#">FAQ</a>
  <a class="donate" href="#">DONATE</a>
</nav>

<div class="abs hero" role="img" aria-label="Man in a suit holding out car keys in front of a parking lot of cars"></div>

<form class="abs donor-form">
  <h2>DONOR INFORMATION</h2>
  <p style="top:27px">Please fill out this form and we'll schedule you for a pick up right away.</p>
  <div class="field" style="left:96px;top:44px;width:146px">Name</div>
  <div class="field" style="left:246px;top:44px;width:156px">Street Address</div>
  <div class="field" style="left:406px;top:44px;width:68px">City</div>
  <div class="field" style="left:478px;top:44px;width:68px">State</div>
  <div class="field" style="left:550px;top:44px;width:68px">Zip Code</div>
  <p style="top:73px">If your vehicle is at a different location, please provide detailed information:</p>
  <div class="field" style="left:96px;top:92px;width:123px">Pick Up Street Address</div>
  <div class="field" style="left:225px;top:92px;width:53px">Pick Up City</div>
  <div class="field" style="left:283px;top:92px;width:53px">Pick Up State</div>
  <div class="field" style="left:342px;top:92px;width:53px">Pick Up Zip</div>
  <div class="field" style="left:399px;top:92px;width:111px">Email Address</div>
  <div class="field" style="left:514px;top:92px;width:59px">Day Phone</div>
  <div class="field" style="left:577px;top:92px;width:41px">Vin</div>
  <div class="field" style="left:96px;top:115px;width:54px">Evening Phone</div>
  <div class="field" style="left:155px;top:115px;width:54px">Vehicle Year</div>
  <div class="field" style="left:213px;top:115px;width:54px">Vehicle Make</div>
  <div class="field" style="left:272px;top:115px;width:53px">Vehicle Model</div>
  <div class="field sel" style="left:329px;top:115px;width:37px">Color</div>
  <div class="field sel" style="left:370px;top:115px;width:44px">Running</div>
  <div class="field sel" style="left:418px;top:115px;width:55px">Body Damage</div>
  <div class="field" style="left:477px;top:115px;width:91px">Notes</div>
  <div class="submit" style="left:572px;top:115px;width:46px">SUBMIT</div>
</form>

<h1 class="abs how-title">HOW DO I <span class="pink">DONATE</span> A VEHICLE OR VESSEL?</h1>
<p class="abs body-text" style="left:108px;top:414px;width:498px">To start, all you need to do is fill out an online application or give us a call! We will forward your information to a local towing company and they will call you right away to pickup your donation. You will receive a donation receipt and if your donation sells for more than $500 you will receive an IRS Tax Form 1098C.</p>
<h2 class="abs sub-title"><span>HOW DOES MY VEHICLE OR VESSEL DONATION BENEFIT</span> Pink Horizon Foundation?</h2>
<p class="abs body-text" style="left:106px;top:473px;width:502px">In these economic times every dollar donated to PH Foundation helps to fund programs serving the homeless and economically disadvantaged. Your donated vehicle or vessel will be sold at auction and the net proceeds will be returned to PH Foundation In these economic times every dollar donated to PH Foundation helps to fund programs serving the homeless and economically disadvantaged. Your donated vehicle or vessel will be sold at auction and the net proceeds will be returned to PH Foundation.</p>

<section class="abs donate-strip">
  <div class="label">Donate :</div>
  <div class="perk" style="left:100px"><svg width="20" height="20" viewBox="0 0 20 20"><path d="M17 10a7 7 0 1 1-2-5" fill="none" stroke="#222" stroke-width="1.6"/><path d="M15 2v3.5h-3.5" fill="none" stroke="#222" stroke-width="1.4"/><text x="10" y="12.5" font-size="6.5" font-weight="700" text-anchor="middle" font-family="Roboto Condensed">24</text></svg><span>FAST FREE PICKUP<br>24HR RESPONSE</span></div>
  <div class="perk" style="left:256px"><svg width="16" height="20" viewBox="0 0 16 20"><rect x="1.5" y="1" width="13" height="18" fill="none" stroke="#222" stroke-width="1.4"/><path d="M4 5h8M4 8h8M4 15h8" stroke="#222"/><text x="8" y="13" font-size="5" text-anchor="middle" font-weight="700">$</text></svg><span>TAX DEDUCTION<br>EASY TO DO!</span></div>
  <div class="perk" style="left:396px"><svg width="24" height="20" viewBox="0 0 24 20"><path d="M2 14h18l-2-5h-5l-3-5H5z" fill="#222"/><circle cx="6" cy="16" r="2.5" fill="#222"/><circle cx="17" cy="16" r="2.5" fill="#222"/></svg><span>RUNNING OR NOT<br>NO EMISSION TEST REQUIRED</span></div>
</section>

<h2 class="abs why-title"><span class="soft">WHY</span> <span class="pink">DONATE</span><br>A VEHICLE OR<br>VESSELS</h2>
<ul class="abs why-list">
  <li><svg width="9" height="9" viewBox="0 0 10 10"><circle cx="5" cy="5" r="4" fill="none" stroke="#e6136f"/><path d="M3 5l1.6 1.6L8 2.5" fill="none" stroke="#e6136f" stroke-width="1.2"/></svg><b>Free pickup,</b> whether the vehicle or vessel is running or not.</li>
  <li><svg width="9" height="9" viewBox="0 0 10 10"><circle cx="5" cy="5" r="4" fill="none" stroke="#e6136f"/><path d="M3 5l1.6 1.6L8 2.5" fill="none" stroke="#e6136f" stroke-width="1.2"/></svg><b>No hassles!</b> No calls, questions, or price haggling to sell your car or boat.</li>
  <li><svg width="9" height="9" viewBox="0 0 10 10"><circle cx="5" cy="5" r="4" fill="none" stroke="#e6136f"/><path d="M3 5l1.6 1.6L8 2.5" fill="none" stroke="#e6136f" stroke-width="1.2"/></svg><b>No strangers</b> coming to your home, no worries about liability, no emissions check required.</li>
  <li><svg width="9" height="9" viewBox="0 0 10 10"><circle cx="5" cy="5" r="4" fill="none" stroke="#e6136f"/><path d="M3 5l1.6 1.6L8 2.5" fill="none" stroke="#e6136f" stroke-width="1.2"/></svg><b>No cost!</b> You won't need to do minor repairs, pay for an ad to sell your item, or pay for an emissions check.</li>
  <li><svg width="9" height="9" viewBox="0 0 10 10"><circle cx="5" cy="5" r="4" fill="none" stroke="#e6136f"/><path d="M3 5l1.6 1.6L8 2.5" fill="none" stroke="#e6136f" stroke-width="1.2"/></svg><b>Avoid confusing</b> paperwork, title transfers, etc.</li>
  <li><svg width="9" height="9" viewBox="0 0 10 10"><circle cx="5" cy="5" r="4" fill="none" stroke="#e6136f"/><path d="M3 5l1.6 1.6L8 2.5" fill="none" stroke="#e6136f" stroke-width="1.2"/></svg><b>Qualifies</b> for IRS Tax Deduction.</li>
</ul>

<section class="abs faq" role="img" aria-label="Cupped hands holding a pink ribbon, in deep plum tones">
  <h2>FREQUENTLY ASKED QUESTIONS</h2>
  <div class="rule"></div>
  <div class="faq-card" style="left:96px">
    <div><span class="plus">+</span>WHY DONATE A VEHICLE OR VESSEL?</div>
    <div><span class="plus">+</span>HOW DO I DONATE A VEHICLE OR VESSEL?</div>
    <div><span class="plus">+</span>HOW DOES MY VEHICLE OR VESSEL DONATION BENEFIT THE CHARITY?</div>
    <div><span class="plus">+</span>HOW DOES DONATING A CAR OR BOAT BENEFIT MY TAXES?</div>
  </div>
  <div class="faq-card" style="left:369px">
    <div><span class="plus">+</span>HOW LONG DOES IT TAKE TO PICKUP MY DONATION?</div>
    <div><span class="plus">+</span>WHAT HAPPENS TO MY CAR AFTER IT'S PICKED UP?</div>
    <div><span class="plus">+</span>DO I HAVE ANY LIABILITY AFTER THE VEHICLE/VESSEL IS PICKED UP?</div>
    <div style="color:var(--pink);position:relative"><span class="plus">≡</span>READ MORE<svg class="abs" style="right:9px;top:11px" width="4" height="5" viewBox="0 0 4 5"><path d="M0 0l4 2.5L0 5z" fill="#222"/></svg></div>
  </div>
</section>

<div class="abs logo-band"><div class="brand"><span class="brand-dot"></span>Rides for Pink Ribbon Aid</div></div>

<footer class="abs site-footer">
  <h3 style="left:96px">Navigation</h3>
  <ul class="foot-nav"><li>Donate a Car or Boat Now</li><li>About Us</li><li>Contact Us</li><li>FAQ</li></ul>
  <h3 style="left:194px">About Rides for Pink Ribbon Aid</h3>
  <p class="about">The Pink Horizon Foundation is committed to making a positive difference in the lives of those afflicted with breast cancer as well as those families affected by breast cancer. The Pink Horizon Foundation financially supports a variety of programs dedicated to breast cancer screening and prevention, treatment and patient health and well-being.</p>
  <div class="contact-box">
    <p>☎ Phone: <span class="val">+1-555-240-7713</span></p>
    <p>✉ E-mail: <span class="val" style="font-size:5.5px">info@ridesforpinkribbonaid.org</span></p>
    <div class="social"><span style="background:#2aa3dc"></span><span style="background:#3b5a99"></span><span style="background:#3f729b"></span><span style="background:#dc4a38"></span></div>
  </div>
</footer>
<div class="abs copyright">© Copyright 2018 Rides for Pink Ribbon Aid, Allrights are Reserved.</div>

</body>
</html>
```